New business blog needs wordpress theme

I need a unique wordpress theme for my new business oriented blog at quietharlow.net. The blog focuses on my experience as an entrepreneur and offers insights into business problems while chronicling my experience building a new company.

I would like to see a theme that looks more like a creative professional's website, not a business website. Large photos, bright colors, unique layout. I do not want stock photos of people in suits doing business type things. Also, no pictures of me - I am blogging anonymously.

The design should communicate technology and beauty - for example, I really like the feel of the landing page at www.pebblyn.net - it is beautiful to look at but also reflects the cutting edge nature of what they are doing.

Industry/Entity Type

Business

```html
<!DOCTYPE html>
<html lang="en">
<head>
<meta charset="utf-8">
<title>quietharlow</title>
<link rel="stylesheet" href="https://fonts.googleapis.com/css2?family=Cabin:wght@400;700&family=Rokkitt:wght@300&family=Cantarell:wght@400;700&display=swap">
<style>
  :root {
    --ink: #000000;
    --logo: #d2d2d2;
    --nav: #ffffff;
    --panel: rgba(255, 255, 255, 0.62);
    --frame: #6e3b1e;
    --heading: #474343;
    --body: #2e2a28;
    --bar: #231b1b;
    --bar-text: #ffffff;
    --footer: #121212;
    --footer-text: #a9a9a9;
    --tile: #2b2b2b;
    --tile-text: #f2f2f2;
  }
  * { box-sizing: border-box; margin: 0; padding: 0; }
  html, body { width: 1200px; height: 787px; overflow: hidden; background: var(--ink); }
  .page { position: relative; width: 1200px; height: 787px; }

  .site-header { position: absolute; left: 0; top: 0; width: 1200px; height: 160px; background: var(--ink); }
  .brand {
    position: absolute; left: 0; right: 0; top: 22px; text-align: center;
    font-family: "Cabin", sans-serif; font-weight: 700; font-size: 52px;
    letter-spacing: 1px; color: var(--logo); line-height: 64px;
  }
  .main-nav { position: absolute; top: 102px; left: 0; width: 1200px; height: 20px; }
  .main-nav a {
    position: absolute; font-family: "Cabin", sans-serif; font-size: 14px;
    color: var(--nav); text-decoration: none; line-height: 20px;
  }

  .hero {
    position: absolute; left: 0; top: 160px; width: 1200px; height: 582px;
    background:
      radial-gradient(ellipse at 88% 20%, rgba(255, 226, 150, 0.85), rgba(255, 200, 110, 0) 45%),
      linear-gradient(90deg, #3a2a22 0%, #5a4436 25%, #8a7560 55%, #c2ab80 80%, #d9c194 100%);
  }
  .hero::after {
    content: ""; position: absolute; inset: 0;
    background: linear-gradient(180deg, rgba(0,0,0,0) 55%, rgba(30,20,15,0.55) 100%);
  }

  .feature {
    position: absolute; left: 279px; top: 338px; width: 684px; height: 351px;
    background: var(--panel);
  }
  .feature-frame {
    position: absolute; left: 10px; top: 11px; width: 664px; height: 329px;
    border: 3px solid var(--frame);
  }
  .feature h1 {
    position: absolute; left: 60px; top: 40px;
    font-family: "Rokkitt", serif; font-weight: 300; font-size: 38px;
    letter-spacing: 1px; color: var(--heading); line-height: 44px;
  }
  .feature p {
    position: absolute; left: 60px; width: 540px;
    font-family: "Cantarell", sans-serif; font-size: 12.5px; line-height: 18px; color: var(--body);
  }
  .intro { top: 95px; }
  .detail { top: 148px; left: 63px !important; }

  .action-bar {
    position: absolute; left: 64px; top: 269px; width: 532px; height: 47px;
    background: var(--bar); font-family: "Cantarell", sans-serif; font-weight: 700;
    font-size: 13px; color: var(--bar-text); line-height: 47px;
  }
  .action-bar a { position: absolute; color: var(--bar-text); text-decoration: none; }
  .action-bar .divider { position: absolute; left: 278px; }

  .social { position: absolute; left: 963px; top: 341px; width: 40px; }
  .social a {
    display: block; width: 38px; height: 42px; margin-bottom: 7px;
    background: var(--tile); border-radius: 6px;
    font-family: "Cabin", sans-serif; font-size: 9px; color: var(--tile-text);
    text-align: center; line-height: 42px; text-decoration: none;
  }

  .site-footer {
    position: absolute; left: 0; top: 742px; width: 1200px; height: 45px;
    background: var(--footer); text-align: center;
    font-family: Arial, Helvetica, sans-serif; font-size: 13px;
    color: var(--footer-text); line-height: 48px;
  }
  .site-footer span { position: relative; left: 33px; }
</style>
</head>
<body>
<div class="page">
  <header class="site-header">
    <div class="brand">quietharlow</div>
    <nav class="main-nav">
      <a href="#" style="left:476px">Home</a>
      <a href="#" style="left:542px">Posts</a>
      <a href="#" style="left:598px">Contact</a>
      <a href="#" style="left:659px">Blogs</a>
      <a href="#" style="left:707px">About</a>
    </nav>
  </header>

  <section class="hero" role="img" aria-label="Sunlit city street at an intersection with traffic lights, brick buildings and parked cars"></section>

  <article class="feature">
    <div class="feature-frame"></div>
    <h1>Lorem ipsum dolor</h1>
    <p class="intro">ipsum dolor sit amet, consectetur adipiscing elit. Duis et dolor orci. Curabitur dolor velit, accumsan eget est vitae, tempor mollis purus. Integer consectetur massa....</p>
    <p class="detail">iDuis autem vel eum iriure dolor in hendrerit in vulputate velit esse molestie consequat, vel illum dolore eu feugiat nulla facilisis at vero eros et accumsan et iusto odio dignissim qui blandit praesent luptatum zzril delenit augue duis dolore te feugait nulla facilisi. See some shortcodes.</p>
    <div class="action-bar">
      <a href="#" style="left:25px">About The Professional Blog Post</a>
      <span class="divider">|</span>
      <a href="#" style="left:328px">Read More Blog Posts</a>
    </div>
  </article>

  <nav class="social" aria-label="Social links">
    <a href="#">Folk</a>
    <a href="#">Reel</a>
    <a href="#">Guild</a>
    <a href="#">Board</a>
  </nav>

  <footer class="site-footer"><span>Copyright 2014 Powered by QuietHarlow. All Rights Reserved.</span></footer>
</div>
</body>
</html>
```